Electrical needs letterhead design

Need a letterhead design for an electrical company. Using the same colours as to what are used in the logo.
After a modern design.

Want the logo in top right or top left.

Must include...

ABN 61 842 307 194
PHONE 0492357018
www.voltarnex.com.au
ben@voltarnex.com.au

'ABN' and 'PHONE' in bold.

Keep it basic. Logo top left, details either next to it or far right corner. Dont want any other objects included.

```html
<!DOCTYPE html>
<html lang="en">
<head>
<meta charset="UTF-8">
<title>Voltarnex Letterhead</title>
<link href="https://fonts.googleapis.com/css2?family=Questrial&family=Mulish:wght@400;800&display=swap" rel="stylesheet">
<style>
  :root {
    --backdrop: #ebebeb;
    --paper: #f9f9f8;
    --brand-red: #a8281e;
    --ink: #4a4a4a;
    --paper-shadow: rgba(0, 0, 0, 0.12);
  }
  html, body {
    margin: 0;
    padding: 0;
    width: 1200px;
    height: 936px;
    overflow: hidden;
    background: var(--backdrop);
  }
  .canvas {
    position: relative;
    width: 1200px;
    height: 936px;
    display: flex;
    align-items: center;
    justify-content: center;
  }
  .letterhead {
    position: relative;
    width: 620px;
    height: 876px;
    background: var(--paper);
    box-shadow: 0 6px 24px var(--paper-shadow);
  }
  .contact {
    position: absolute;
    top: 60px;
    left: 0;
    display: flex;
    align-items: flex-end;
  }
  .contact-bar {
    width: 36px;
    height: 28px;
    background: var(--brand-red);
    margin-right: 12px;
  }
  .contact-list {
    margin: 0;
    padding: 0;
    list-style: none;
    font-family: "Mulish", sans-serif;
    font-size: 9px;
    line-height: 11px;
    color: var(--ink);
  }
  .contact-label {
    font-weight: 800;
    color: var(--brand-red);
  }
  .brand {
    position: absolute;
    top: 58px;
    right: 40px;
    display: flex;
    align-items: center;
    gap: 9px;
  }
  .brand-mark {
    width: 13px;
    height: 13px;
    border-radius: 50%;
    background: var(--brand-red);
  }
  .brand-name {
    font-family: "Questrial", sans-serif;
    font-size: 40px;
    color: var(--brand-red);
    letter-spacing: 0.5px;
    line-height: 1;
  }
</style>
</head>
<body>
  <main class="canvas">
    <section class="letterhead">
      <div class="contact">
        <div class="contact-bar"></div>
        <ul class="contact-list">
          <li><span class="contact-label">Phone:</span> 0492357018</li>
          <li><span class="contact-label">Email:</span> ben@voltarnex.com.au</li>
          <li><span class="contact-label">ABN:</span> 61 842 307 194</li>
          <li><span class="contact-label">Web:</span> www.voltarnex.com.au</li>
        </ul>
      </div>
      <header class="brand">
        <span class="brand-mark"></span>
        <span class="brand-name">Voltarnex</span>
      </header>
    </section>
  </main>
</body>
</html>
```